Accounting business needs a fridge magnet design

I need a business card size design to be used as a fridge magnet.
It will need to be vertical not horizontal and it will have my logo and the services I provide listed below it.
It needs to be pleasing to the eye and catch peoples attention.
I have uploaded my current business card as a reference.
It can look totally different though, i am open to new ideas.

It will need to say:

Specialising in:
*Small Business Taxation
*Company & Trust Returns
*Financial Statements
*Partnership Taxation
*BAS preparation/lodgement
*Capital Gains Tax
*Business Start Ups
*Business Structuring
*Tax Planning

```html
<!DOCTYPE html>
<html lang="en">
<head>
<meta charset="utf-8">
<title>Norvale Tax – Fridge Magnet</title>
<link rel="stylesheet" href="https://fonts.googleapis.com/css2?family=Poppins:wght@400;500;600&family=Roboto+Condensed:wght@400&display=swap">
<style>
  :root {
    --backdrop: #8e8e8e;
    --card: #ffffff;
    --ink: #222222;
    --ink-soft: #333333;
    --ring: #2b2b2b;
    --ghost: #ececec;
    --badge-green: #c4d600;
    --badge-ring: #9a9a9a;
  }
  * { margin: 0; padding: 0; box-sizing: border-box; }
  html, body {
    width: 1200px;
    height: 1200px;
    overflow: hidden;
    background: var(--backdrop);
  }
  .magnet {
    position: absolute;
    left: 269px;
    top: 60px;
    width: 662px;
    height: 1080px;
    background: var(--card);
    overflow: hidden;
    font-family: "Poppins", sans-serif;
    color: var(--ink);
  }
  .ghost-ring {
    position: absolute;
    left: 297px;
    top: 706px;
    width: 418px;
    height: 418px;
    border: 7px solid var(--ghost);
    border-radius: 50%;
  }
  .brand-ring {
    position: absolute;
    left: 241px;
    top: 96px;
    width: 178px;
    height: 178px;
    border: 4px solid var(--ring);
    border-radius: 50%;
  }
  .brand-name {
    position: absolute;
    left: 0;
    right: 0;
    top: 314px;
    text-align: center;
    white-space: nowrap;
    font-weight: 600;
    font-size: 48px;
    line-height: 60px;
    letter-spacing: 0.2em;
    padding-left: 0.2em;
    color: var(--ink);
  }
  .services {
    position: absolute;
    left: 68px;
    top: 398px;
    font-size: 29px;
    line-height: 37.8px;
    color: var(--ink-soft);
    list-style: none;
    white-space: nowrap;
  }
  .services-heading {
    font-weight: 600;
    color: #111;
  }
  .badge {
    position: absolute;
    left: 67px;
    top: 817px;
    width: 146px;
    height: 146px;
  }
  .agent-number {
    position: absolute;
    left: 60px;
    width: 160px;
    top: 972px;
    text-align: center;
    font-family: "Roboto Condensed", sans-serif;
    font-size: 17px;
    line-height: 22px;
    color: #333;
  }
</style>
</head>
<body>
  <div class="magnet">
    <div class="ghost-ring"></div>
    <div class="brand-ring"></div>
    <div class="brand-name">NORVALE TAX</div>

    <ul class="services">
      <li class="services-heading">SPECIALISING IN:</li>
      <li>*Small Business Taxation</li>
      <li>*Company &amp; Trust Returns</li>
      <li>*Financial Statements</li>
      <li>*Partnership Taxation</li>
      <li>*BAS preparation/lodgement</li>
      <li>*Capital Gains Tax</li>
      <li>*Business Start Ups</li>
      <li>*Business Structuring</li>
      <li>*Tax Planning</li>
    </ul>

    <svg class="badge" viewBox="0 0 146 146" role="img" aria-label="Registration badge">
      <circle cx="73" cy="73" r="71" fill="#fff" stroke="var(--badge-ring)" stroke-width="2"/>
      <circle cx="73" cy="73" r="44" fill="var(--badge-green)"/>
    </svg>
    <div class="agent-number">Tax agent<br>31057286</div>
  </div>
</body>
</html>
```